General Dental Office Business Card

I run a private general dental office in southern California, and would like a refresh/redesign of my business card. I focus on quality care rather than volume. The email address on the uploaded current card should be updated to: info@marbleshoredental.example. The current card's logo is a deboss, but I am open to other ideas. The logo can be refreshed, but it is something that's been with me since the beginning of the office, so I wouldn't want a drastic redesign.
Target Market(s)
Adults 18-99, whoever needs dental services
Industry/Entity Type
Healthcare/Dental
Contact Information for Business Card
Name, Address, Phone, email
Colors
Designer to choose colors to be used in the design.
Requirements
Must have
- Logo (Same as original one in the uploaded file), space on back for appointment time/date

```html
<!DOCTYPE html>
<html lang="en">
<head>
<meta charset="utf-8">
<title>Marble Shore Dental – Business Card</title>
<link href="https://fonts.googleapis.com/css2?family=Arimo:wght@400;700&display=swap" rel="stylesheet">
<style>
  :root{
    --sky:#85d5eb;
    --white:#ffffff;
    --slate:#707070;
    --ink:#6b6b6b;
    --dash:#a8a8a8;
    --page:#d9d9d9;
  }
  *{box-sizing:border-box;margin:0;padding:0}
  html,body{width:1125px;height:1200px;overflow:hidden}
  body{background:var(--page);font-family:"Arimo",Arial,sans-serif;position:relative}
  .card{position:absolute;left:152px;width:820px;height:470px;border-radius:22px;overflow:hidden;background:var(--white);box-shadow:0 3px 6px rgba(0,0,0,.25)}
  .card--front{top:98px;background:var(--sky)}
  .card--back{top:630px}
  .card svg.shape{position:absolute;inset:0}

  .front-info{position:absolute;left:32px;top:66px;color:var(--white)}
  .doctor-name{font-size:32px;font-weight:700;letter-spacing:.2px}
  .specialty{font-size:20px;margin-top:8px}
  .rule{width:315px;height:2px;background:var(--white);margin:28px 0 30px}
  .address{font-size:20px;line-height:32px}
  .contact{list-style:none;font-size:20px}
  .contact li{display:flex;align-items:center;gap:10px;height:33px}
  .contact svg{width:18px;height:18px;flex:none}

  .brand{position:absolute;left:475px;top:140px;width:345px;text-align:center;color:var(--sky)}
  .brand-dot{width:150px;height:150px;border-radius:50%;background:var(--sky);margin:0 auto 18px}
  .brand-name{font-size:44px;line-height:50px;font-weight:400;letter-spacing:1px}

  .back-band{position:absolute;left:0;top:0;width:100%;height:168px;background:var(--sky)}
  .back-brand{position:absolute;top:0;left:0;width:100%;height:168px;display:flex;align-items:center;justify-content:center;gap:14px;color:var(--white)}
  .back-brand .brand-dot{width:40px;height:40px;margin:0;background:var(--white)}
  .back-brand span{font-size:34px;letter-spacing:1px}
  .back-stripe{position:absolute;left:0;top:173px;width:100%;height:6px;background:var(--slate)}
  .tab{position:absolute;left:210px;top:173px;width:400px;height:38px}
  .tab-label{position:absolute;left:210px;top:181px;width:400px;text-align:center;color:var(--white);font-size:22px}
  .fill-line{position:absolute;left:54px;width:712px;border-top:2px dashed var(--dash)}
  .days{position:absolute;left:115px;top:350px;display:flex;gap:24px;color:var(--ink);font-size:22px}
  .opt{display:flex;align-items:center;gap:9px}
  .box{width:17px;height:17px;border:2px solid var(--sky)}
  .when{position:absolute;left:127px;top:387px;display:flex;align-items:center;gap:14px;color:var(--ink);font-size:22px}
  .blank{display:inline-block;border-bottom:2px solid var(--ink);height:22px}
</style>
</head>
<body>

<section class="card card--front">
  <svg class="shape" viewBox="0 0 820 470" aria-hidden="true">
    <path d="M538 0 Q366 235 538 470 L820 470 L820 0Z" fill="#ffffff"/>
    <path d="M546 0 Q380 235 546 470 L820 470 L820 0Z" fill="#707070"/>
    <path d="M565 0 Q408 235 565 470 L820 470 L820 0Z" fill="#ffffff"/>
  </svg>
  <div class="front-info">
    <h1 class="doctor-name">Daniel R. Moss DDS</h1>
    <p class="specialty">General Dentistry</p>
    <div class="rule"></div>
    <p class="address">2180 Harbor Crest Way<br>Coastview, CA 92000</p>
    <div class="rule"></div>
    <ul class="contact">
      <li><svg viewBox="0 0 24 24"><path d="M6 3l4 4-2 3a12 12 0 006 6l3-2 4 4-3 3C10 21 3 14 3 6z" fill="none" stroke="#fff" stroke-width="2"/></svg>555-014-2828</li>
      <li><svg viewBox="0 0 24 24"><rect x="2" y="5" width="20" height="14" rx="2" fill="none" stroke="#fff" stroke-width="2"/><path d="M2 6l10 7 10-7" fill="none" stroke="#fff" stroke-width="2"/></svg>info@marbleshoredental.example</li>
      <li><svg viewBox="0 0 24 24"><circle cx="12" cy="12" r="10" fill="none" stroke="#fff" stroke-width="2"/><ellipse cx="12" cy="12" rx="4" ry="10" fill="none" stroke="#fff" stroke-width="2"/><path d="M2 12h20" stroke="#fff" stroke-width="2"/></svg>www.marbleshoredental.example</li>
    </ul>
  </div>
  <div class="brand">
    <div class="brand-dot"></div>
    <p class="brand-name">Marble Shore<br>Dental</p>
  </div>
</section>

<section class="card card--back">
  <div class="back-band"></div>
  <div class="back-brand"><div class="brand-dot"></div><span>Marble Shore Dental</span></div>
  <div class="back-stripe"></div>
  <svg class="tab" viewBox="0 0 400 38" aria-hidden="true"><path d="M0 0H400L372 38H28Z" fill="#707070"/></svg>
  <p class="tab-label">APPOINTMENT</p>
  <div class="fill-line" style="top:266px"></div>
  <div class="fill-line" style="top:318px"></div>
  <div class="days">
    <span class="opt"><i class="box"></i>MON</span>
    <span class="opt"><i class="box"></i>TUE</span>
    <span class="opt"><i class="box"></i>WED</span>
    <span class="opt"><i class="box"></i>THU</span>
    <span class="opt"><i class="box"></i>FRI</span>
    <span class="opt"><i class="box"></i>SAT</span>
  </div>
  <div class="when">
    <span>DATE</span><span class="blank" style="width:158px"></span>
    <span>TIME</span><span class="blank" style="width:106px"></span>
    <span class="opt"><i class="box"></i>AM</span>
    <span class="opt"><i class="box"></i>PM</span>
  </div>
</section>

</body>
</html>
```